Create the artwork for Wavelantern's debut album, 'Under Paper Lanterns'!

We are a cinematic pop/jazz quartet from Oslo/London looking for someone to create the artwork for our debutalbum, 'Under Paper Lanterns'. This is a project we are incredibly proud of, and we are looking for the perfect artwork to complement our music.

We want the artwork to convey the organic feel of our sound, yet be eye-catching with bright colours. Attached are several examples for inspiration. The title of the album, 'Under Paper Lanterns', should be an inspiration for the design in a subtle/abstract way. Think out of the box here, we are not looking for a hundred solar system designs.

You can find an album teaser here for inspiration: https://tunebarrow.example/wavelanternsound/album-teaser

This is our webpage: wavelanternsound.example

Excited to see what you come up with and to work with some brilliant creatives !

Much love,

Wavelantern
Updates

Everyone, thanks for your effort and great designs! We're discussing right now and will get back to you with feedback and suggested edits very shortly. Thanks for your patience! Much love, Wavelantern

Requirements
Must have
• Ready-to-print high-res files in standard CD Cover format
• Artwork ready for digital release on spotify, iTunes, and social media channels
Nice to have
• Would love to have smaller extensions of the artwork (pattern or pieces of art in same theme) to use on webpage/social media channels.

```html
<!DOCTYPE html>
<html lang="en">
<head>
<meta charset="utf-8">
<title>Wavelantern — Under Paper Lanterns</title>
<link rel="stylesheet" href="https://fonts.googleapis.com/css2?family=Josefin+Sans:wght@300&display=swap">
<style>
  :root {
    --paper: #ffffff;
    --ink: #161616;
    --magenta: #a3124f;
    --crimson: #d81f3c;
    --cream: #f4eedb;
    --butter: #f2df7a;
    --peach: #eeb49a;
    --coral: #e4553a;
    --teal: #1f8c9c;
  }
  html, body {
    margin: 0;
    padding: 0;
    width: 1200px;
    height: 1200px;
    overflow: hidden;
    background: var(--paper);
  }
  .album-cover {
    position: relative;
    width: 1200px;
    height: 1200px;
    background: var(--paper);
    font-family: "Josefin Sans", sans-serif;
    color: var(--ink);
  }
  .masthead {
    position: absolute;
    top: 80px;
    left: 122px;
    right: 120px;
    height: 100px;
    display: flex;
    align-items: center;
  }
  .band-name {
    display: flex;
    align-items: center;
    gap: 10px;
    font-weight: 300;
    font-size: 20px;
    letter-spacing: 0.5px;
  }
  .band-name .mark {
    width: 14px;
    height: 14px;
    border: 1.5px solid var(--ink);
    border-radius: 50%;
  }
  .album-title {
    margin: 0 0 0 48px;
    font-weight: 300;
    font-size: 50px;
    letter-spacing: 8px;
    white-space: nowrap;
    line-height: 1;
  }
  .artwork {
    position: absolute;
    left: 22px;
    top: 238px;
    width: 1156px;
    height: 938px;
    display: block;
  }
</style>
</head>
<body>
  <main class="album-cover">
    <header class="masthead">
      <div class="band-name"><span class="mark"></span>Wavelantern</div>
      <h1 class="album-title">UNDER PAPER LANTERNS</h1>
    </header>

    <svg class="artwork" viewBox="0 0 1156 938" role="img" aria-label="Abstract poured-paint artwork: pools of magenta, crimson, cream, butter yellow and peach colliding, with a teal streak in the lower right">
      <defs>
        <radialGradient id="pour-left" cx="20%" cy="30%" r="60%">
          <stop offset="0" stop-color="var(--coral)"/>
          <stop offset="0.5" stop-color="var(--magenta)"/>
          <stop offset="1" stop-color="var(--magenta)" stop-opacity="0"/>
        </radialGradient>
        <radialGradient id="pour-right" cx="78%" cy="22%" r="45%">
          <stop offset="0" stop-color="var(--butter)"/>
          <stop offset="1" stop-color="var(--butter)" stop-opacity="0"/>
        </radialGradient>
        <radialGradient id="pour-red" cx="90%" cy="62%" r="30%">
          <stop offset="0" stop-color="var(--crimson)"/>
          <stop offset="1" stop-color="var(--crimson)" stop-opacity="0"/>
        </radialGradient>
        <radialGradient id="pour-teal" cx="92%" cy="95%" r="22%">
          <stop offset="0" stop-color="var(--teal)"/>
          <stop offset="1" stop-color="var(--teal)" stop-opacity="0"/>
        </radialGradient>
        <linearGradient id="pour-base" x1="0" y1="0" x2="1" y2="1">
          <stop offset="0" stop-color="var(--cream)"/>
          <stop offset="0.6" stop-color="var(--peach)"/>
          <stop offset="1" stop-color="var(--butter)"/>
        </linearGradient>
      </defs>
      <rect width="1156" height="938" fill="url(#pour-base)"/>
      <rect width="1156" height="938" fill="url(#pour-left)"/>
      <rect width="1156" height="938" fill="url(#pour-right)"/>
      <rect width="1156" height="938" fill="url(#pour-red)"/>
      <rect width="1156" height="938" fill="url(#pour-teal)"/>
    </svg>
  </main>
</body>
</html>
```